Bloom Where You Stand redesign book cover

A new cover for my already published book. The old cover looks great but not for a women’s self help book. Cover is killing sales. Once I explain the book it sells quickly AND gets 5 star reviews. Outside of actually explaining the book the cover scares people away. I need a new cover. ASAP! Before The yr end please.
The tag line -
Discover 10 Simple Habits to exchange anxious thinking for hearing the calm voice of grace. This is a self help book for women 35-45 Christian but not religious. Each chapter is a hands on spiritual experience where the reader takes small tests about themselves, discover why they have negative thoughts, what they are and how to listen to God through hands on methods of listening. NOT strange type of things. They learn what 4 voices they are listening to and how to hone in on Jesus voice. There are scriptures to pray and journaling assignments. The old cover is in the brief with the write up for the back of the book. Please use the new author picture, Publishers logo (tree), barcode, and contact info from the back of the book. And yes the author name and title of the book on the spine. Lay out on the back cover needs to be interesting. You have all the info have fun with it.

Target Market(s)

Women 35-45 yrs old Christian and new believers or seekers.

Industry/Entity Type

Non profit organization. Missionary

Requirements
Must have
• Something DIFFERENT than what is there now. Something inviting. Fresh clear title
Nice to have
• Multi colors however a white stand out cover is also good.
Should not have
• Heavy religious feeling. No church steeples, Jesus faces.

```html
<!DOCTYPE html>
<html lang="en">
<head>
<meta charset="utf-8">
<title>Bloom Where You Stand — Book Cover</title>
<link rel="stylesheet" href="https://fonts.googleapis.com/css2?family=Cormorant+Garamond:wght@300;400&family=Lato:wght@400;700&display=swap">
<style>
  :root {
    --sky-top: #dcdde6;
    --sky-mid: #e9e3e2;
    --glow: #f3d9bf;
    --haze: #b9c3cc;
    --sea: #6f8796;
    --sea-deep: #3f5566;
    --tagline: #3d6777;
    --title: #f6e9e0;
    --author: #ffffff;
  }
  html, body {
    margin: 0;
    padding: 0;
    overflow: hidden;
    background: #ffffff;
  }
  .cover {
    position: relative;
    width: 857px;
    height: 1200px;
    overflow: hidden;
  }
  .cover-photo {
    position: absolute;
    inset: 0;
    background:
      radial-gradient(ellipse 520px 200px at 50% 540px, var(--glow) 0%, rgba(243, 217, 191, 0) 70%),
      linear-gradient(180deg,
        var(--sky-top) 0%,
        var(--sky-mid) 30%,
        #e7d8d0 44%,
        var(--haze) 52%,
        var(--sea) 68%,
        var(--sea-deep) 100%);
  }
  .tagline {
    position: absolute;
    top: 26px;
    left: 0;
    right: 0;
    margin: 0;
    text-align: center;
    font-family: "Lato", sans-serif;
    font-weight: 700;
    font-size: 30px;
    line-height: 57px;
    letter-spacing: 0.3px;
    color: var(--tagline);
  }
  .title {
    position: absolute;
    top: 640px;
    left: 0;
    right: 0;
    margin: 0;
    text-align: center;
    font-family: "Cormorant Garamond", serif;
    font-weight: 300;
    color: var(--title);
    text-transform: uppercase;
  }
  .title-line {
    display: block;
  }
  .title-main {
    font-size: 152px;
    line-height: 150px;
    letter-spacing: 16px;
    padding-left: 16px;
  }
  .title-small {
    font-size: 32px;
    line-height: 47px;
    letter-spacing: 4px;
    padding-left: 4px;
  }
  .author {
    position: absolute;
    top: 1070px;
    left: 0;
    right: 0;
    margin: 0;
    text-align: center;
    font-family: "Lato", sans-serif;
    font-weight: 700;
    font-size: 36px;
    line-height: 48px;
    letter-spacing: 6px;
    color: var(--author);
    text-transform: uppercase;
  }
</style>
</head>
<body>
  <main class="cover">
    <div class="cover-photo" role="img" aria-label="Photograph of a hand holding up a single feather against a soft sunset sky over a blurred sea"></div>

    <p class="tagline">10 Simple Habits to exchange anxious thinking<br>for hearing the calm voice of grace</p>

    <h1 class="title">
      <span class="title-line title-main">Bloom</span>
      <span class="title-line title-small">Where You</span>
      <span class="title-line title-main">Stand</span>
    </h1>

    <p class="author">Dana Whitcombe</p>
  </main>
</body>
</html>
```